Product labels for new supplements business targeting high performing creative people

I need a label design for different supplements like Whey, BCAA, Melatonin etc. that I could customize for each use case separately.

The brand is called lanternfolk.life, and it would be the first design of the labels. We haven't sold any products yet, but the target audience is people with growth mindset, people who want to be as efficient as possible and are constantly looking to improve their lifestyle. As part of that, they are also working out, but don't know much about supplements yet. Mostly people between 20-34.

I don't have a too specific idea of the expected design, though it should be light, warm, smart and minimalist, maybe have some patterns. It should looks smart and clean (and expensive). Orange and golden might be the additional colors for white. I have attached the templates of some products that I plan to sell and also the logo of the brand.

Here's what I have used for inspiration:
Brands that I like and are somewhat similar in concept: https://www.vimqera.com/ (!!specially the way they
bring "how the product helps them" in focus, not "what the product is" & https://www.pobri.care/ &
https://www.selvoda.com/sport/ & https://en.kambelo.fr/ &
https://gridmarket.com/profiles/corawellhaldesign/designs/417586

Here's how different products look like: https://prodaxel.com/catalog

Target Market(s)

target audience is people with growth mindset, people who want to be as efficient as possible and are constantly looking to improve their lifestyle. As part of that, they are also working out, but don't know much about supplements yet. Mostly people between 20-34.

Industry/Entity Type

Supplements

Font styles to use
Sans Serif

Colors
FFC000
F8CF3A
FAE287
FDF2CF
FEFAEE
F0912C
F2A743
F7CA91
FBE8D2
FDF5EE
EE7325
F08F49
F5BC92
FAE3D3
FDF4ED

Requirements
Must have
• Clean, smart and minimalist design that can be applied for different products in different sizes, like Whey protein, BCAA, vitamins etc. available here: https://prodaxel.com/catalog
Nice to have
• Patterns, expensive look
Should not have
• Doodles, too many colors

```html
<!DOCTYPE html>
<html lang="en">
<head>
<meta charset="UTF-8">
<title>lanternfolk.life — Supplement Label Range</title>
<link rel="stylesheet" href="https://fonts.googleapis.com/css2?family=Montserrat:wght@400;500;600;800;900&display=swap">
<style>
  :root {
    --page: #fafafa;
    --label-white: #ffffff;
    --label-mist: #e9e9e9;
    --ink: #2b2b2b;
    --ink-soft: #444444;
    --orange: #ee7325;
    --orange-mid: #f08f49;
    --orange-light: #f5bc92;
    --gold: #f2a743;
    --yellow: #f8cf3a;
    --yellow-soft: #fae287;
    --cream: #fdf2cf;
  }
  * { box-sizing: border-box; margin: 0; padding: 0; }
  html, body { width: 988px; height: 1200px; overflow: hidden; }
  body {
    background: var(--page);
    font-family: "Montserrat", sans-serif;
    color: var(--ink);
    position: relative;
  }
  .label {
    position: absolute;
    display: flex;
    flex-direction: column;
    background: var(--label-white);
    box-shadow: 0 6px 18px rgba(0,0,0,0.08);
    overflow: hidden;
  }
  .label__info {
    display: flex;
    flex-direction: column;
    align-items: center;
    text-align: center;
    background: linear-gradient(90deg, var(--label-white) 0%, var(--label-mist) 30%, var(--label-mist) 70%, var(--label-white) 100%);
  }
  .brand {
    display: flex;
    align-items: center;
    gap: 4px;
    font-weight: 500;
    color: var(--ink);
    letter-spacing: 0.01em;
  }
  .brand__dot {
    width: 7px; height: 7px;
    border-radius: 50%;
    background: var(--orange);
  }
  .product-name {
    font-weight: 900;
    color: var(--orange-mid);
    line-height: 1;
    letter-spacing: -0.01em;
    white-space: nowrap;
  }
  .product-variant {
    font-weight: 800;
    color: var(--orange-mid);
    letter-spacing: 0.12em;
    line-height: 1.2;
  }
  .product-type {
    font-weight: 500;
    letter-spacing: 0.14em;
    color: var(--ink);
  }
  .benefits {
    font-weight: 400;
    color: var(--ink-soft);
    line-height: 1.25;
  }
  .pattern {
    flex: 1;
    position: relative;
    background:
      linear-gradient(135deg, var(--orange) 0%, var(--orange-mid) 25%, var(--yellow-soft) 45%, var(--orange-light) 60%, var(--gold) 80%, var(--yellow) 100%);
  }
  .amount-tag {
    position: absolute;
    left: 50%;
    bottom: 0;
    transform: translateX(-50%);
    background: var(--yellow-soft);
    color: var(--ink);
    font-weight: 500;
    white-space: nowrap;
    padding: 2px 6px 1px;
  }

  /* Melatonin */
  .label--melatonin { left: 157px; top: 215px; width: 192px; height: 303px; }
  .label--melatonin .label__info { height: 128px; padding-top: 3px; }
  .label--melatonin .brand { font-size: 12px; }
  .label--melatonin .product-name { font-size: 26px; margin-top: 17px; }
  .label--melatonin .product-type { font-size: 8.5px; margin-top: 2px; }
  .label--melatonin .benefits { font-size: 9.5px; margin-top: 12px; }
  .label--melatonin .amount-tag { font-size: 9.5px; }

  /* Beef protein */
  .label--beef { left: 606px; top: 233px; width: 240px; height: 233px; }
  .label--beef .label__info { height: 112px; padding-top: 12px; }
  .label--beef .brand { font-size: 12px; }
  .label--beef .product-name { font-size: 22px; margin-top: 10px; }
  .label--beef .product-variant { font-size: 7.5px; }
  .label--beef .product-type { font-size: 7.5px; margin-top: 6px; }
  .label--beef .benefits { font-size: 7.5px; margin-top: 2px; }
  .label--beef .amount-tag { font-size: 8px; }

  /* Maca root */
  .label--maca { left: 156px; top: 864px; width: 215px; height: 241px; }
  .label--maca .label__info { height: 121px; padding-top: 16px; background: var(--label-white); }
  .label--maca .brand { font-size: 11.5px; }
  .label--maca .product-name { font-size: 26px; margin-top: 12px; }
  .label--maca .product-variant { font-size: 7.5px; margin-top: 2px; }
  .label--maca .product-type { font-size: 7px; }
  .label--maca .benefits { font-size: 6.5px; margin-top: 4px; }
  .label--maca .amount-tag { font-size: 6.5px; bottom: 10px; }

  /* BCAA */
  .label--bcaa { left: 580px; top: 785px; width: 286px; height: 355px; }
  .label--bcaa .label__info { height: 180px; padding-top: 26px; }
  .label--bcaa .brand { font-size: 14px; }
  .label--bcaa .product-name { font-size: 28px; margin-top: 36px; }
  .label--bcaa .product-variant { font-size: 9px; margin-top: 2px; }
  .label--bcaa .product-type { font-size: 9px; margin-top: 7px; }
  .label--bcaa .benefits { font-size: 9px; margin-top: 7px; }
  .label--bcaa .amount-tag { font-size: 9.5px; bottom: 8px; }
</style>
</head>
<body>
  <main class="label-range">

    <article class="label label--melatonin">
      <header class="label__info">
        <div class="brand"><span class="brand__dot"></span>lanternfolk.life</div>
        <h2 class="product-name">MELATONIN</h2>
        <p class="product-type">DIETARY SUPPLEMENT</p>
        <p class="benefits">Fall asleep faster*<br>Stay asleep longer*</p>
      </header>
      <div class="pattern" role="img" aria-label="Geometric pattern of orange and golden circles, triangles and diamonds">
        <span class="amount-tag">60 TABLETS</span>
      </div>
    </article>

    <article class="label label--beef">
      <header class="label__info">
        <div class="brand"><span class="brand__dot"></span>lanternfolk.life</div>
        <h2 class="product-name">BEEF PROTEIN</h2>
        <p class="product-variant">CHOCOLATE</p>
        <p class="product-type">DIETARY SUPPLEMENT</p>
        <p class="benefits">Hydrolized beef protein with minimum<br>fat content lorem ipsum lorem ipsum</p>
      </header>
      <div class="pattern" role="img" aria-label="Geometric pattern of orange and golden circles, triangles and diamonds">
        <span class="amount-tag">Net Wt. 900g (31.075OZ)</span>
      </div>
    </article>

    <article class="label label--maca">
      <header class="label__info">
        <div class="brand"><span class="brand__dot"></span>lanternfolk.life</div>
        <h2 class="product-name">MACA ROOT</h2>
        <p class="product-variant">POWDER</p>
        <p class="product-type">DIETARY SUPPLEMENT</p>
        <p class="benefits">Helps reduce stress*<br>Increases energy and stamina*</p>
      </header>
      <div class="pattern" role="img" aria-label="Geometric pattern of orange and golden circles, triangles and diamonds">
        <span class="amount-tag">200 g</span>
      </div>
    </article>

    <article class="label label--bcaa">
      <header class="label__info">
        <div class="brand"><span class="brand__dot"></span>lanternfolk.life</div>
        <h2 class="product-name">BCAA 2:1:1</h2>
        <p class="product-variant">WILD BERRY</p>
        <p class="product-type">DIETARY SUPPLEMENT</p>
        <p class="benefits">Hydrolized beef protein with minimum<br>fat content lorem ipsum lorem ipsum</p>
      </header>
      <div class="pattern" role="img" aria-label="Geometric pattern of orange and golden circles, triangles and diamonds">
        <span class="amount-tag">Net Wt. 300g (10.58OZ)</span>
      </div>
    </article>

  </main>
</body>
</html>
```